Innovative Bitcoin Powerpoint Presentation

I have constructred most of the data for a 15 page powerpoint presentation on an innovative bitcoin idea that provides access to fiat currency with bitcoin hodlings

I need this to look great as a first blush to potential investors

Reason: updated deck and name

Target Market(s)

Venture Capital firms and private equity firms

Requirements
Must have
• Fun, innovateive deck, very clean
Should not have
• any generic feel - no templates

```html
<!DOCTYPE html>
<html lang="en">
<head>
<meta charset="utf-8">
<title>Ledgerly Investor Deck</title>
<link href="https://fonts.googleapis.com/css2?family=Roboto+Condensed:wght@300;400;700&family=Open+Sans:wght@400&display=swap" rel="stylesheet">
<style>
  :root{
    --ink:#1e1e1e;
    --ink-soft:#3a3a3a;
    --orange:#f7941d;
    --orange-deep:#f07d0f;
    --amber:#f6a623;
    --gold:#f5c638;
    --pale:#fde49c;
    --grey:#6e6e6e;
    --grey-light:#9e9e9e;
    --paper:#f4f4f4;
    --white:#ffffff;
    --stage:#000000;
  }
  *{box-sizing:border-box;margin:0;padding:0}
  html,body{width:1058px;height:1200px;overflow:hidden;background:var(--stage)}
  .stage{position:absolute;left:0;top:0;width:1095px;height:1242px;transform:scale(0.9662);transform-origin:0 0}
  .slide{position:absolute;width:518px;height:388px;background:var(--paper);overflow:hidden;font-family:"Roboto Condensed",sans-serif;color:var(--ink)}
  .slide--tall{height:392px}
  .hero-art{position:absolute;left:0;top:0;width:100%;background:radial-gradient(circle at 55% 20%,#ffd86a 0,rgba(255,216,106,0) 30%),linear-gradient(160deg,#f9a826 0%,#f7901c 55%,#f6a23a 100%)}
  .header-band{position:absolute;left:0;top:0;width:100%;height:48px;background:linear-gradient(180deg,#f8a52a 0%,#f9b444 55%,#fcd98f 100%)}
  .slide-title{position:absolute;left:14px;top:11px;font-weight:700;font-size:20px;color:var(--ink)}
  .brand{position:absolute;right:5px;top:11px;font-weight:700;font-size:22px;letter-spacing:.3px;color:#fff6dc}
  .footer{position:absolute;left:0;bottom:0;width:518px;height:18px}
  .divider{position:absolute;width:1px;background:var(--grey-light)}
  .project-title{position:absolute;font-weight:700;color:var(--ink)}
  .presenter{position:absolute;font-size:11px;color:var(--ink)}
  .subtext{position:absolute;font-size:9.5px;line-height:15px;color:var(--ink-soft)}
  .cover-brand{position:absolute;left:193px;top:263px;font-weight:700;font-size:22px;color:var(--orange)}
  .emblem{position:absolute;left:118px;top:192px;width:80px;height:80px;border:5px solid var(--white);border-radius:50%;display:flex;align-items:center;justify-content:center;font-weight:700;font-size:13px;color:var(--white)}
  .lead{position:absolute;left:32px;top:76px;font-family:"Open Sans",sans-serif;font-size:10.5px;color:var(--ink)}
  .chart{position:absolute;left:0;top:0}
  .chart text{font-family:"Open Sans",sans-serif;font-size:7.5px;fill:var(--ink)}
  .points{position:absolute;left:28px;top:82px;list-style:none}
  .point{position:relative;padding-left:20px;font-size:14px;color:var(--ink);height:28px;line-height:18px}
  .point--sub{padding-left:44px;font-size:12.5px;height:19px;line-height:16px}
  .point svg{position:absolute;left:0;top:3px}
  .point--sub svg{left:34px;top:4px}
  .stat{position:absolute;width:114px}
  .stat-value{height:56px;display:flex;align-items:center;justify-content:center;font-weight:300;font-size:32px;color:var(--white);box-shadow:0 1px 3px rgba(0,0,0,.25)}
  .stat-link{width:2px;height:40px;margin:0 auto;background:var(--grey-light)}
  .stat-label{height:59px;border:2px solid;background:var(--white);display:flex;align-items:center;justify-content:center;text-align:center;font-size:15px;line-height:19px;color:var(--ink-soft)}
  .stat--orange .stat-value{background:var(--amber)}
  .stat--orange .stat-label{border-color:var(--amber)}
  .stat--gold .stat-value{background:var(--gold)}
  .stat--gold .stat-label{border-color:var(--gold)}
  .stat--grey .stat-value{background:var(--grey)}
  .stat--grey .stat-label{border-color:var(--grey)}
</style>
</head>
<body>
<div class="stage">

  <!-- Cover, light -->
  <section class="slide" style="left:20px;top:15px">
    <div class="hero-art" style="height:193px" role="img" aria-label="Orange abstract network of glowing nodes and lines"></div>
    <div class="cover-brand">LEDGERLY</div>
    <div class="divider" style="left:300px;top:232px;height:90px"></div>
    <div class="project-title" style="left:317px;top:232px;font-size:23px">Project Title Here</div>
    <div class="presenter" style="left:318px;top:267px">Marcus Hale</div>
    <div class="subtext" style="left:318px;top:291px;width:185px">Subtext here Subtext here Subtext here Subtext here Subtext here Subtext here</div>
    <svg class="footer" viewBox="0 0 518 18"><polygon points="0,6 372,6 360,18 0,18" fill="#9e9e9e"/><polygon points="372,0 518,0 518,18 354,18" fill="#f7941d"/></svg>
  </section>

  <!-- Cover, full colour -->
  <section class="slide slide--tall" style="left:558px;top:15px">
    <div class="hero-art" style="height:392px" role="img" aria-label="Orange abstract network of glowing nodes and lines"></div>
    <div class="emblem">LEDGERLY</div>
    <div class="divider" style="left:210px;top:178px;height:104px;background:#8a4a00"></div>
    <div class="project-title" style="left:222px;top:178px;font-size:26px">Project Title Here</div>
    <div class="presenter" style="left:223px;top:218px;font-size:12px">Marcus Hale</div>
    <div class="subtext" style="left:223px;top:241px;width:210px;font-size:10.5px;line-height:16px;color:var(--ink)">Subtext here Subtext here Subtext here Subtext here Subtext here Subtext here</div>
  </section>

  <!-- Bar chart -->
  <section class="slide" style="left:20px;top:423px">
    <div class="header-band" role="img" aria-label="Orange header with soft network glow"></div>
    <h2 class="slide-title">Higher Rate of Innovation</h2>
    <div class="brand">LEDGERLY</div>
    <p class="lead">Lorem ipsum dolor sit ipsum Lorem ipsum dolor sit ipsum Lorem ipsum Lorem ipsum</p>
    <svg class="chart" width="518" height="388" viewBox="0 0 518 388">
      <text x="30" y="133">Lorem ipsum text here</text>
      <text x="30" y="164">Lorem ipsum text here</text>
      <text x="30" y="203">Lorem ipsum text here</text>
      <text x="30" y="253">Lorem ipsum text here</text>
      <text x="30" y="311">Lorem ipsum text here</text>
      <rect x="118" y="249" width="22" height="61" fill="#9b9b9b"/>
      <rect x="145" y="199" width="26" height="111" fill="#f3aa2e"/>
      <rect x="178" y="220" width="26" height="90" fill="#fde39a"/>
      <rect x="210" y="256" width="26" height="54" fill="#f7be52"/>
      <rect x="243" y="294" width="28" height="16" fill="#f3b650"/>
      <rect x="277" y="305" width="32" height="5" fill="#777"/>
      <rect x="313" y="137" width="27" height="173" fill="#f3ad35"/>
      <rect x="346" y="293" width="28" height="17" fill="#fde39a"/>
      <rect x="379" y="302" width="28" height="8" fill="#f7be52"/>
      <line x1="118" y1="122" x2="118" y2="310" stroke="#555" stroke-width="1"/>
      <line x1="118" y1="310" x2="446" y2="310" stroke="#555" stroke-width="1"/>
      <text x="117" y="327">Lorem ipsum text here</text>
      <text x="230" y="327">Lorem ipsum text here</text>
      <text x="366" y="327">Lorem ipsum text here</text>
    </svg>
    <svg class="footer" viewBox="0 0 518 18"><polygon points="0,6 372,6 360,18 0,18" fill="#9e9e9e"/><polygon points="372,0 518,0 518,18 354,18" fill="#f7941d"/></svg>
  </section>

  <!-- Bullet points -->
  <section class="slide" style="left:558px;top:423px">
    <div class="header-band" role="img" aria-label="Orange header with soft network glow"></div>
    <h2 class="slide-title">Project Title Here</h2>
    <div class="brand">LEDGERLY</div>
    <ul class="points">
      <li class="point"><svg width="14" height="12" viewBox="0 0 14 12"><path d="M1 6 L5 10 L13 1" fill="none" stroke="#f7941d" stroke-width="2.4"/></svg>Secured line of credit leveraging BTC collateral</li>
      <li class="point point--sub"><svg width="6" height="9" viewBox="0 0 6 9"><path d="M1 1 L5 4.5 L1 8" fill="none" stroke="#f7941d" stroke-width="1.8"/></svg>Reduces BTC currency exchange costs</li>
      <li class="point point--sub" style="height:27px"><svg width="6" height="9" viewBox="0 0 6 9"><path d="M1 1 L5 4.5 L1 8" fill="none" stroke="#f7941d" stroke-width="1.8"/></svg>Mitigates price volatility risk</li>
      <li class="point"><svg width="14" height="12" viewBox="0 0 14 12"><path d="M1 6 L5 10 L13 1" fill="none" stroke="#f7941d" stroke-width="2.4"/></svg>$300m credit facility secured</li>
      <li class="point point--sub" style="height:28px"><svg width="6" height="9" viewBox="0 0 6 9"><path d="M1 1 L5 4.5 L1 8" fill="none" stroke="#f7941d" stroke-width="1.8"/></svg>Provided by one of the worlds largest P/E firms</li>
      <li class="point"><svg width="14" height="12" viewBox="0 0 14 12"><path d="M1 6 L5 10 L13 1" fill="none" stroke="#f7941d" stroke-width="2.4"/></svg>Global opportunity</li>
      <li class="point"><svg width="14" height="12" viewBox="0 0 14 12"><path d="M1 6 L5 10 L13 1" fill="none" stroke="#f7941d" stroke-width="2.4"/></svg>Scalable API integration</li>
      <li class="point"><svg width="14" height="12" viewBox="0 0 14 12"><path d="M1 6 L5 10 L13 1" fill="none" stroke="#f7941d" stroke-width="2.4"/></svg>First to market advantage</li>
    </ul>
    <svg class="footer" viewBox="0 0 518 18"><polygon points="0,6 372,6 360,18 0,18" fill="#9e9e9e"/><polygon points="372,0 518,0 518,18 354,18" fill="#f7941d"/></svg>
  </section>

  <!-- Line chart -->
  <section class="slide" style="left:20px;top:840px">
    <div class="header-band" role="img" aria-label="Orange header with soft network glow"></div>
    <h2 class="slide-title">Higher Rate of Innovation</h2>
    <div class="brand">LEDGERLY</div>
    <svg class="chart" width="518" height="388" viewBox="0 0 518 388">
      <g stroke="#555" stroke-width="1">
        <line x1="110" y1="104" x2="110" y2="309"/>
        <line x1="110" y1="309" x2="418" y2="309"/>
        <line x1="106" y1="104" x2="110" y2="104"/><line x1="106" y1="133" x2="110" y2="133"/>
        <line x1="106" y1="162" x2="110" y2="162"/><line x1="106" y1="192" x2="110" y2="192"/>
        <line x1="106" y1="221" x2="110" y2="221"/><line x1="106" y1="250" x2="110" y2="250"/>
        <line x1="106" y1="280" x2="110" y2="280"/>
        <line x1="213" y1="309" x2="213" y2="313"/><line x1="315" y1="309" x2="315" y2="313"/>
      </g>
      <g text-anchor="end">
        <text x="100" y="107">14</text><text x="100" y="136">12</text><text x="100" y="165">10</text>
        <text x="100" y="195">8</text><text x="100" y="224">6</text><text x="100" y="253">4</text>
        <text x="100" y="283">2</text><text x="100" y="312">0</text>
      </g>
      <text x="157" y="322">2</text><text x="261" y="322">4</text><text x="364" y="322">6</text>
      <g fill="none" stroke-width="2.2" stroke-linejoin="round">
        <polyline stroke="#d9d4c3" points="110,309 145,253 170,255 210,222 250,215 275,215 300,190 330,197 365,160 412,120"/>
        <polyline stroke="#777" points="110,309 140,260 172,257 198,220 230,217 280,182 310,180 330,170 365,155 412,116"/>
        <polyline stroke="#f37021" points="110,309 165,240 210,232 238,225 272,180 320,175 365,172 372,148 410,112"/>
        <polyline stroke="#f37021" points="110,309 130,298 160,296 220,294 235,298 300,291 330,296 412,297"/>
      </g>
    </svg>
    <svg class="footer" viewBox="0 0 518 18"><polygon points="0,6 372,6 360,18 0,18" fill="#9e9e9e"/><polygon points="372,0 518,0 518,18 354,18" fill="#f7941d"/></svg>
  </section>

  <!-- Market size -->
  <section class="slide" style="left:558px;top:840px">
    <div class="header-band" role="img" aria-label="Orange header with soft network glow"></div>
    <h2 class="slide-title">Market Size</h2>
    <div class="brand">LEDGERLY</div>
    <div class="stat stat--orange" style="left:33px;top:134px">
      <div class="stat-value">13.5m</div><div class="stat-link"></div><div class="stat-label">BTC IN<br>CIRCULATION</div>
    </div>
    <div class="stat stat--gold" style="left:202px;top:134px">
      <div class="stat-value">13.5m</div><div class="stat-link"></div><div class="stat-label">BTC IN<br>CIRCULATION</div>
    </div>
    <div class="stat stat--grey" style="left:371px;top:134px">
      <div class="stat-value">13.5m</div><div class="stat-link"></div><div class="stat-label">BTC IN<br>CIRCULATION</div>
    </div>
    <svg class="footer" viewBox="0 0 518 18"><polygon points="0,6 372,6 360,18 0,18" fill="#9e9e9e"/><polygon points="372,0 518,0 518,18 354,18" fill="#f7941d"/></svg>
  </section>

</div>
</body>
</html>
```